Pitch Deck Redesign

Our company is currently in need of our pitch deck to be revamped and made much cleaner. We have a solid foundation and framework and now just need a final polishing.
We are looking to hire a freelance graphic designer that we can create a long-term relationship with. We want to be able to utilize this person week after week for various projects and designs. Designs will need to be delivered to our team both as png that will slide ride into a wide view powerpoint presentation and will need to supply original design file (PSD).
Thank you in advance for your responses and time,
Niles
It Company

```html
<!DOCTYPE html>
<html lang="en">
<head>
<meta charset="utf-8">
<title>Bridges Slide</title>
<link rel="stylesheet" href="https://fonts.googleapis.com/css2?family=Jost:wght@400;500;700&display=swap">
<style>
  :root {
    --page: #ffffff;
    --frame: #a9a9a9;
    --accent-sky: #9ad8f1;
    --stat-red: #b51c1c;
    --stat-navy: #12508b;
    --text-navy: #1d5796;
    --photo-green: #4d6b3a;
    --photo-river: #4a3f2c;
    --photo-concrete: #b9b3a6;
  }
  html, body {
    margin: 0;
    padding: 0;
    width: 1200px;
    height: 1200px;
    overflow: hidden;
    background: var(--page);
  }
  .slide {
    position: absolute;
    left: 54px;
    top: 294px;
    width: 1092px;
    height: 613px;
    background: var(--page);
    border: 1px solid var(--frame);
    box-sizing: border-box;
    overflow: hidden;
    font-family: "Jost", sans-serif;
  }
  .corner-accent {
    position: absolute;
    left: 0;
    display: block;
  }
  .corner-accent--top { top: 0; }
  .corner-accent--bottom { bottom: 0; }
  .headline {
    position: absolute;
    left: 96px;
    top: 18px;
    margin: 0;
    display: flex;
    align-items: baseline;
    white-space: nowrap;
    line-height: 1;
  }
  .headline__fraction {
    font-weight: 700;
    font-size: 80px;
    color: var(--stat-red);
    letter-spacing: 1px;
  }
  .headline__of {
    font-weight: 500;
    font-size: 26px;
    color: var(--stat-navy);
    margin-left: 30px;
  }
  .headline__total {
    font-weight: 700;
    font-size: 80px;
    color: var(--stat-navy);
    margin-left: 12px;
  }
  .headline__label {
    font-weight: 400;
    font-size: 26px;
    color: var(--text-navy);
    margin-left: 10px;
  }
  .hero-photo {
    position: absolute;
    left: 0;
    top: 120px;
    width: 100%;
    height: 374px;
    background:
      linear-gradient(170deg, rgba(77,107,58,0.9) 0%, rgba(185,179,166,0.7) 35%, rgba(74,63,44,0.9) 60%, rgba(77,107,58,0.85) 100%),
      var(--photo-concrete);
  }
  .source-note {
    position: absolute;
    right: 28px;
    bottom: 24px;
    margin: 0;
    font-size: 14px;
    font-weight: 400;
    color: var(--text-navy);
  }
</style>
</head>
<body>
  <section class="slide">
    <svg class="corner-accent corner-accent--top" width="104" height="120" viewBox="0 0 104 120" aria-hidden="true">
      <polygon points="0,0 104,0 48,120 0,120" fill="var(--accent-sky)"/>
    </svg>
    <h1 class="headline">
      <span class="headline__fraction">1/4</span>
      <span class="headline__of">of</span>
      <span class="headline__total">600,000</span>
      <span class="headline__label">bridges are structurally deficient</span>
    </h1>
    <div class="hero-photo" role="img" aria-label="Aerial photograph of a collapsed highway bridge lying in a river beside an intact arched bridge"></div>
    <svg class="corner-accent corner-accent--bottom" width="136" height="118" viewBox="0 0 136 118" aria-hidden="true">
      <polygon points="0,0 84,0 136,118 0,118" fill="var(--accent-sky)"/>
    </svg>
    <p class="source-note">*Civic Report 2016</p>
  </section>
</body>
</html>
```